Pale Lanterns Old Lane Walk Poster Design

We need an A4 sized poster to promote our weekly true crime tours. This poster will be posted onto community noticeboards.
Lots of information and images can be viewed at the following links:-
www.palelanterns.com.au
www.palelanterns.com.au/bookings/
https://www.facebook.com/palelanternsoldlane/
https://www.examplereviews.com.au/Attraction_Review-g000000-d00000000-Reviews-Pale_Lanterns-Newcastle_Greater_Newcastle_New_South_Wales.html
There are also a number of images for possible use at the following link - we are open to intepretation:-
http://palelanterns.com.au/tour-photographs/
The font on our website is "SpecialElite" so we would like to continue using that font type.
Target Market(s)
Adults 25-65.
Font styles to use
Other font styles liked:
- Special Elite
Colors
Designer to choose colors to be used in the design.
Look and feel
Each slider illustrates characteristics of the customer's brand and the style your logo design should communicate.

```html
<!DOCTYPE html>
<html lang="en">
<head>
<meta charset="utf-8">
<title>Pale Lanterns Old Lane Walk Poster</title>
<link rel="stylesheet" href="https://fonts.googleapis.com/css2?family=Special+Elite&display=swap">
<style>
  :root {
    --backdrop: #2b2d30;
    --brand-red: #bd1f1d;
    --ink: #1b1b1b;
    --paper-light: #f1dcaa;
    --paper-mid: #e6c48a;
    --paper-edge: #d9a86a;
    --photo-light: #b9b9b9;
    --photo-mid: #6f6f6f;
    --photo-dark: #1e1e1e;
    --tag-grey: #d8d3c6;
    --white: #ffffff;
  }
  * { margin: 0; padding: 0; box-sizing: border-box; }
  html, body {
    width: 1200px; height: 1200px; overflow: hidden;
    background: var(--backdrop);
    font-family: "Special Elite", "Courier New", monospace;
  }
  .poster {
    position: absolute; left: 203px; top: 39px;
    width: 794px; height: 1122px; overflow: hidden;
    background: radial-gradient(ellipse at 50% 60%, var(--paper-light) 0%, var(--paper-mid) 70%, var(--paper-edge) 100%);
  }
  .poster__photo {
    position: absolute; left: 0; top: 40px; width: 794px; height: 490px;
    background:
      radial-gradient(ellipse at 60% 25%, var(--photo-light) 0%, transparent 55%),
      linear-gradient(180deg, var(--photo-mid) 0%, #4a4a4a 45%, #3a3a3a 70%, var(--photo-dark) 100%);
  }
  .poster__edges { position: absolute; left: 0; top: 0; width: 794px; height: 1122px; }
  .edge-red { fill: var(--brand-red); }
  .edge-paper { fill: url(#paperFill); }

  .brand {
    position: absolute; left: 0; top: 640px; width: 794px;
    display: flex; justify-content: center; align-items: center; gap: 12px;
  }
  .brand__dot { width: 16px; height: 16px; border-radius: 50%; background: var(--ink); }
  .brand__name { font-size: 34px; color: var(--ink); letter-spacing: 1px; }

  .title { position: absolute; left: 0; width: 794px; text-align: center; line-height: 1; font-weight: normal; }
  .title--main { top: 738px; font-size: 68px; color: var(--ink); }
  .title--sub { top: 814px; font-size: 60px; color: var(--brand-red); }

  .book-tag {
    position: absolute; left: 284px; top: 902px; width: 222px; height: 42px;
    background: var(--tag-grey); color: var(--ink);
    font-size: 27px; text-align: center; line-height: 44px;
  }
  .tour-name {
    position: absolute; left: 0; top: 952px; width: 794px; text-align: center;
    font-size: 27px; color: var(--brand-red); letter-spacing: .5px;
  }
  .contact {
    position: absolute; top: 1010px; display: flex; align-items: center; gap: 14px; color: var(--ink);
  }
  .contact--phone { left: 64px; font-size: 31px; }
  .contact--email { left: 352px; font-size: 22px; }
  .contact__icon {
    width: 28px; height: 28px; border-radius: 50%;
    border: 2px solid var(--brand-red); display: flex; align-items: center; justify-content: center;
  }
  .contact__icon svg { width: 15px; height: 15px; fill: var(--brand-red); }

  .footer-band {
    position: absolute; left: 0; top: 1055px; width: 794px; height: 67px;
    background: var(--brand-red); color: var(--white);
    text-align: center; font-size: 29px; line-height: 67px;
  }
</style>
</head>
<body>
  <main class="poster">
    <div class="poster__photo" role="img" aria-label="Black and white photograph of a rainy old city street with a tram and a lone figure crossing"></div>

    <svg class="poster__edges" viewBox="0 0 794 1122" aria-hidden="true">
      <defs>
        <radialGradient id="paperFill" cx="50%" cy="60%" r="70%">
          <stop offset="0" stop-color="#f1dcaa"/>
          <stop offset=".7" stop-color="#e6c48a"/>
          <stop offset="1" stop-color="#d9a86a"/>
        </radialGradient>
      </defs>
      <polygon class="edge-red" points="0,0 794,0 794,55 760,62 730,52 700,63 660,57 620,67 580,60 540,71 500,63 460,73 420,78 380,71 340,81 300,75 260,85 220,79 180,90 140,85 110,96 80,89 50,101 30,94 0,100"/>
      <polygon class="edge-paper" points="0,522 30,512 60,519 100,507 140,515 180,503 220,511 260,499 300,507 340,495 380,503 420,493 460,501 500,489 540,497 580,485 620,493 660,481 700,489 740,477 770,485 794,476 794,1122 0,1122"/>
    </svg>

    <div class="brand">
      <span class="brand__dot"></span>
      <span class="brand__name">PALE LANTERNS</span>
    </div>

    <h1 class="title title--main">PALE LANTERNS</h1>
    <h2 class="title title--sub">OLD LANE WALK</h2>

    <div class="book-tag">BOOK NOW -</div>
    <p class="tour-name">WHISPERS FROM THE GASLIT YARD</p>

    <div class="contact contact--phone">
      <span class="contact__icon">
        <svg viewBox="0 0 24 24"><path d="M6.6 10.8a15.1 15.1 0 0 0 6.6 6.6l2.2-2.2c.3-.3.7-.4 1-.2 1.1.4 2.3.6 3.6.6.6 0 1 .4 1 1V20c0 .6-.4 1-1 1A17 17 0 0 1 3 4c0-.6.4-1 1-1h3.5c.6 0 1 .4 1 1 0 1.3.2 2.5.6 3.6.1.3 0 .7-.2 1z"/></svg>
      </span>
      <span>0412555019</span>
    </div>
    <div class="contact contact--email">
      <span class="contact__icon">
        <svg viewBox="0 0 24 24"><path d="M2 5h20v14H2zM4 7v.5l8 5 8-5V7l-8 5z"/></svg>
      </span>
      <span>INFO@PALELANTERNS.COM.AU</span>
    </div>

    <footer class="footer-band">WWW.PALELANTERNS.COM.AU</footer>
  </main>
</body>
</html>
```